Automotive component supplier needs a business card design

We need a business card design for our company called Velmar Global Components Ltd based in the UK. We are a supplier of interior and exterior components to premium car manufacturers such as Corvane Hale, Durrant Fyfe, Maxtorn and Valdessimo. We would like to see a modern business card design that uses the colour blue.

Target Market(s)

Premium automotive car manufacturers.

Industry/Entity Type

Automotive

Contact Information for Business Card

Company Name : Velmar Global Components Limited
Address: 17 Tamsey Yard, Upper Drisk, Warwick, CV31 8RJ, United Kingdom
Web Address : www.velmarparts-example.co.uk

Font styles to use
Other font styles liked:
• Helvetica

Colors
3176b5
0255a3
85acd3
cfdeed
cee9f5
85cae6
34a6d7
0692cd
9bcb3c

Requirements
Must have
• Clear company logo and a mixture of blue colours.
Nice to have
• A high quality modern image.
Should not have
• Multiple colours.

```html
<!DOCTYPE html>
<html lang="en">
<head>
<meta charset="utf-8">
<title>Velmar Global Components – Business Card</title>
<link rel="stylesheet" href="https://fonts.googleapis.com/css2?family=Arimo:wght@400;700&family=Michroma&display=swap">
<style>
  :root {
    --stage: #1c1c1e;
    --card: #050505;
    --blue: #0692cd;
    --green: #9bcb3c;
  }
  * { margin: 0; padding: 0; box-sizing: border-box; }
  html, body { width: 1200px; height: 900px; overflow: hidden; }
  body {
    background: var(--stage);
    font-family: "Arimo", Helvetica, Arial, sans-serif;
    display: flex; flex-direction: column; align-items: center; justify-content: center;
    gap: 40px;
  }
  .card {
    position: relative;
    width: 640px; height: 366px;
    background: var(--card);
    overflow: hidden;
    box-shadow: 0 12px 30px rgba(0,0,0,.5);
  }
  .rule { position: absolute; height: 6px; background: var(--green); }

  /* front */
  .front .brand {
    position: absolute; left: 0; right: 0; top: 110px;
    display: flex; align-items: center; justify-content: center; gap: 14px;
  }
  .brand-mark { width: 22px; height: 22px; background: var(--green); border-radius: 4px; }
  .brand-name {
    color: var(--blue); font-weight: 700; font-size: 40px; letter-spacing: 1px;
    text-transform: uppercase;
  }
  .front .rule-upper { left: 392px; right: 0; top: 190px; }
  .front .rule-lower { left: 0; width: 330px; top: 312px; }
  .front .web {
    position: absolute; left: 338px; top: 298px;
    color: var(--blue); font-size: 14px;
  }

  /* back */
  .back .identity { position: absolute; left: 36px; top: 150px; }
  .back .brand-name { font-size: 30px; display: block; }
  .back .tagline {
    color: var(--blue); font-size: 9px; letter-spacing: 1.6px; text-transform: uppercase;
    margin-top: 2px;
  }
  .person {
    font-family: "Michroma", "Arimo", sans-serif;
    color: var(--blue); font-size: 15px; margin-top: 18px; letter-spacing: 1px;
  }
  .role { color: var(--green); font-size: 13px; text-align: right; margin-top: 2px; }
  .divider {
    position: absolute; left: 372px; top: 118px; width: 2px; height: 150px;
    background: var(--green);
  }
  .contact { position: absolute; left: 392px; top: 120px; color: var(--blue); font-size: 13px; line-height: 1.4; }
  .address { margin-bottom: 8px; }
  .contact-list { list-style: none; }
  .contact-list li { display: flex; align-items: center; gap: 8px; }
  .contact-list svg { width: 11px; height: 11px; fill: var(--green); flex: none; }
  .back .rule-bottom { left: 0; right: 0; top: 316px; }
</style>
</head>
<body>
  <section class="card front">
    <div class="brand">
      <span class="brand-name">Velmar</span>
      <span class="brand-mark"></span>
    </div>
    <div class="rule rule-upper"></div>
    <div class="web">www.velmarparts-example.co.uk</div>
    <div class="rule rule-lower"></div>
  </section>

  <section class="card back">
    <div class="identity">
      <span class="brand-name">Velmar</span>
      <div class="tagline">Global Components</div>
      <div class="person">DECLAN MORROW</div>
      <div class="role">Director</div>
    </div>
    <div class="divider"></div>
    <div class="contact">
      <p class="address">17 Tamsey Yard, Upper Drisk<br>Warwick, CV31 8RJ, UK</p>
      <ul class="contact-list">
        <li><svg viewBox="0 0 12 12"><path d="M2 1h2l1 3-1.5 1a7 7 0 0 0 3.5 3.5L8 7l3 1v2a1 1 0 0 1-1 1A9 9 0 0 1 1 2a1 1 0 0 1 1-1z"/></svg>01926 555 014</li>
        <li><svg viewBox="0 0 12 12"><path d="M3 0h6a1 1 0 0 1 1 1v10a1 1 0 0 1-1 1H3a1 1 0 0 1-1-1V1a1 1 0 0 1 1-1zm0 2v7h6V2z"/></svg>07700 900 482</li>
        <li><svg viewBox="0 0 12 12"><path d="M0 2h12v1L6 7 0 3zm0 2.5 6 4 6-4V10H0z"/></svg>hello@velmarparts-example.co.uk</li>
        <li><svg viewBox="0 0 12 12"><circle cx="6" cy="6" r="5.5"/></svg>www.velmarparts-example.co.uk</li>
      </ul>
    </div>
    <div class="rule rule-bottom"></div>
  </section>
</body>
</html>
```